Powerpoint contest

We need to re-design our powerpoints to be much more consistent. All the details are mentioned here. I have more than 30 slides to be created in all.

https://www.pagevault.example/gravik/All-Powerpoints-3c7e91d2ab0f4e6c8d15b27a90e4cf61

Requirements
Must have
• Colors should be greyscale and bravocell pink (ea0a8e) used in small amounts just for accents.

```html
<!DOCTYPE html>
<html lang="en">
<head>
<meta charset="utf-8">
<title>Quorvex master slide presentation</title>
<link href="https://fonts.googleapis.com/css2?family=Montserrat:wght@400;500;600;700;800&display=swap" rel="stylesheet">
<style>
:root{
  --pink:#ea0a8e;
  --ink:#1c1c1c;
  --grey-900:#2b2b2b;
  --grey-600:#6b6b6b;
  --grey-400:#a9a9a9;
  --grey-300:#c9c9c9;
  --grey-200:#dedede;
  --grey-100:#efefef;
  --board:#e3e3e3;
  --white:#ffffff;
}
*{box-sizing:border-box;margin:0;padding:0}
html,body{width:690px;height:1200px;overflow:hidden}
body{background:var(--board);font-family:"Montserrat",sans-serif;color:var(--ink);position:relative}
.slide{position:absolute;width:315px;height:177px;background:var(--white);overflow:hidden;box-shadow:0 4px 8px rgba(0,0,0,.18)}
.c1{left:19px}.c2{left:356px}
.r1{top:21px}.r2{top:217px}.r3{top:413px}.r4{top:609px}.r5{top:805px}.r6{top:1001px}
.a{position:absolute}
.dots{position:absolute;background:radial-gradient(ellipse at 60% 60%,rgba(255,255,255,.95),rgba(225,225,225,.5) 55%,rgba(255,255,255,0) 75%)}
.grad-bg{background:linear-gradient(135deg,#fafafa,#dcdcdc 55%,#f4f4f4)}
.brand{position:absolute;display:flex;align-items:center;font-weight:700;color:var(--ink)}
.brand .mark{border-radius:50%;background:var(--pink);margin-right:.3em}
.hdr{position:absolute;left:0;top:0;width:275px;height:30px;background:linear-gradient(90deg,#fff 10%,#c4c4c4);border-bottom-right-radius:30px}
.hdr h2{position:absolute;left:10px;top:9px;font-size:10px;font-weight:800;letter-spacing:.2px}
.hdr h2 span{color:#fff}
.title-pink{color:var(--pink)}
.lbl{font-size:4.3px;font-weight:600;line-height:1.25}
.sm{font-size:3.6px;line-height:1.3;color:var(--grey-600)}
.pinkcap{font-size:4.6px;font-weight:700;color:var(--pink)}
.card{position:absolute;background:#fff;border-radius:5px;box-shadow:0 1px 4px rgba(0,0,0,.16)}
.dash{position:absolute;border:.6px dashed var(--grey-400);border-radius:5px}
.ico{position:absolute;width:9px;height:9px;border-radius:50%;background:#fff;box-shadow:0 0 2px rgba(0,0,0,.3)}
.ico::after{content:"";position:absolute;left:3px;top:3px;width:3px;height:3px;background:var(--grey-900);border-radius:1px}
.bar{position:absolute;height:4px;border-radius:2px;border:.5px solid var(--grey-300);background:#fff}
.bar i{display:block;height:100%;background:var(--grey-900);border-radius:2px;font-style:normal;color:#fff;font-size:3.2px;font-weight:700;line-height:3.2px;padding-left:2px}
.donut{position:absolute;border-radius:50%;display:flex;align-items:center;justify-content:center;font-size:4px;font-weight:700;background:#fff;box-shadow:0 0 3px rgba(0,0,0,.2)}
.pill{position:absolute;border:.6px solid var(--grey-300);border-radius:5px;background:#fff;font-size:3.6px;font-weight:600;text-align:center;line-height:6px;color:var(--grey-600)}
.pill.pk{color:var(--pink)}
.foot{position:absolute;left:0;bottom:0;width:100%;height:13px;background:var(--grey-100);display:flex;align-items:center;font-size:4px;padding:0 10px;gap:16px}
.foot b{font-weight:700}
.cat{position:absolute;top:52px;width:32px;height:9px;background:var(--grey-900);color:#fff;font-size:3px;font-weight:700;text-align:center;line-height:3.4px;padding-top:1px}
.cat::before{content:"";position:absolute;left:11px;top:-11px;width:10px;height:10px;border-radius:50%;background:var(--grey-600);border:1.5px solid #fff;box-shadow:0 0 2px rgba(0,0,0,.4)}
.logo-col{position:absolute;top:67px;width:32px;display:flex;flex-direction:column;align-items:center;gap:3.4px}
.logo-col i{display:block;height:3px;border-radius:1px;background:var(--grey-400)}
.qa{font-size:4px;line-height:1.3}
.qa b{font-size:6px;font-weight:700}
</style>
</head>
<body>

<!-- Cover -->
<section class="slide c1 r1 grad-bg">
  <div class="dots" role="img" aria-label="Halftone dot wave decoration" style="left:80px;top:40px;width:260px;height:150px"></div>
  <div class="brand" style="left:31px;top:28px;font-size:22px"><span class="mark" style="width:14px;height:14px"></span>Quorvex</div>
  <div class="a" style="right:18px;top:155px;font-size:4px;letter-spacing:2.2px;font-weight:600">WWW.QUORVEX.EXAMPLE</div>
</section>

<!-- Logo slide -->
<section class="slide c2 r1">
  <div class="brand" style="left:11px;top:65px;font-size:27px"><span class="mark" style="width:17px;height:17px"></span>Quorvex</div>
  <div class="foot"><span>www.quorvex.example</span><span>(555) 014 2280</span><span>hello [@] quorvex.example</span><span style="margin-left:auto"><b>CREATED BY</b> quorvex</span></div>
</section>

<!-- Title -->
<section class="slide c1 r2 grad-bg">
  <div class="dots" role="img" aria-label="Halftone dot wave decoration" style="left:-20px;top:-10px;width:200px;height:140px"></div>
  <div class="brand" style="right:20px;top:15px;font-size:11px"><span class="mark" style="width:7px;height:7px"></span>Quorvex</div>
  <div class="a" style="right:18px;top:62px;text-align:right;font-size:13px;font-weight:800;line-height:1.2">MASTER SLIDE<br>PRESENTATION</div>
  <div class="a" style="right:18px;top:94px;font-size:4px;letter-spacing:2px">SUBTITLE GOES HERE</div>
  <div class="a" style="right:18px;top:105px;font-size:4.5px;font-weight:700">May, 2020</div>
  <div class="a" style="left:12px;top:160px;font-size:3.8px;font-weight:600">PRESENTERS &nbsp;| &nbsp;LOREM IPSUM</div>
  <svg class="a" style="right:20px;top:157px" width="24" height="7"><g fill="none" stroke="#333" stroke-width=".5"><circle cx="3.5" cy="3.5" r="3"/><circle cx="12" cy="3.5" r="3"/><circle cx="20.5" cy="3.5" r="3"/></g></svg>
</section>

<!-- Company profile -->
<section class="slide c2 r2">
  <div class="hdr"><h2>COMPANY <span>PROFILE</span></h2></div>
  <div class="a pinkcap" style="left:12px;top:39px">QUORVEX SOLUTIONS</div>
  <div class="ico" style="left:19px;top:55px"></div><div class="a lbl" style="left:35px;top:56px">DevOps &amp; Release<br>management</div>
  <div class="ico" style="left:19px;top:72px"></div><div class="a lbl" style="left:35px;top:75px">Data Migration</div>
  <div class="card" style="left:82px;top:40px;width:93px;height:60px">
    <div class="ico" style="left:10px;top:8px;width:12px;height:12px"></div>
    <div class="a pinkcap" style="left:38px;top:10px">CUSTOMER<br>STATISFACTION</div>
    <div class="a" style="left:17px;top:34px;font-size:6.5px;font-weight:700">103%</div><div class="a sm" style="left:36px;top:36px">Revenue retention</div>
    <div class="a" style="left:14px;top:46px;font-size:6.5px;font-weight:700">98.2%</div><div class="a sm" style="left:36px;top:46px">Customer would recommend<br>Quorvex</div>
  </div>
  <div class="card" style="left:184px;top:38px;width:93px;height:62px">
    <div class="ico" style="left:14px;top:8px;width:12px;height:12px"></div>
    <div class="a pinkcap" style="left:40px;top:10px">REVENUE<br>INVESTMENT</div>
    <div class="a sm" style="left:4px;top:31px;width:46px;text-align:right">Sales &amp; Marketing</div><div class="bar" style="left:52px;top:31px;width:38px"><i style="width:62%">35%</i></div>
    <div class="a sm" style="left:0;top:38px;width:50px;text-align:right">Research &amp; Development</div><div class="bar" style="left:52px;top:38px;width:38px"><i style="width:48%">28%</i></div>
    <div class="a sm" style="left:4px;top:45px;width:46px;text-align:right">Customer Support</div><div class="bar" style="left:52px;top:45px;width:38px"><i style="width:30%">14%</i></div>
    <div class="a sm" style="left:4px;top:52px;width:46px;text-align:right">Retained Earnings</div><div class="bar" style="left:52px;top:52px;width:38px"><i style="width:32%">16%</i></div>
  </div>
  <div class="a lbl" style="left:287px;top:40px;font-size:3.8px">DIVERSITY</div>
  <div class="donut" style="left:288px;top:49px;width:14px;height:14px">43%</div><div class="a sm" style="left:290px;top:65px">Women</div>
  <div class="donut" style="left:288px;top:79px;width:14px;height:14px">45%</div><div class="a sm" style="left:283px;top:95px">Other minorities</div>
  <div class="a pinkcap" style="left:12px;top:97px">COMPANY METRICS</div>
  <div class="a" style="left:12px;top:108px;height:64px;border-left:.6px dashed var(--grey-400)"></div>
  <div class="ico" style="left:19px;top:111px"></div><div class="a lbl" style="left:35px;top:112px">Founded in 2014<br>by an ex-Stratacloud Employee</div>
  <div class="ico" style="left:19px;top:128px"></div><div class="a lbl" style="left:35px;top:131px">Headquartered in Alder Springs, CA</div>
  <div class="ico" style="left:19px;top:143px"></div><div class="a lbl" style="left:35px;top:145px">Two development centers in<br>Eastern Europe and India</div>
  <div class="ico" style="left:19px;top:159px"></div><div class="a lbl" style="left:35px;top:161px">Three support centers in the US,<br>Eastern Europe and India</div>
  <div class="a" role="img" aria-label="World map with office location pins" style="left:112px;top:112px;width:103px;height:58px;border-radius:20px;background:radial-gradient(ellipse,#d4d4d4,#f2f2f2 70%,#fff)"></div>
  <div class="a" style="left:213px;top:108px;height:64px;border-left:.6px dashed var(--grey-400)"></div>
  <div class="a lbl" style="left:219px;top:112px">TEAM STRENGTH</div>
  <div class="a sm" style="left:258px;top:113px">2020</div><div class="bar" style="left:269px;top:113px;width:39px"><i style="width:82%">76 members</i></div>
  <div class="a sm" style="left:258px;top:120px">2019</div><div class="bar" style="left:269px;top:120px;width:39px"><i style="width:40%">59</i></div>
  <div class="a sm" style="left:258px;top:127px">2018</div><div class="bar" style="left:269px;top:127px;width:39px"><i style="width:28%">21</i></div>
  <div class="a pinkcap" style="left:220px;top:141px">PHILANTHROPIC WORK</div>
  <div class="card" style="left:220px;top:153px;width:18px;height:14px;font-size:6px;font-weight:700;text-align:center;line-height:14px">450+</div>
  <div class="a sm" style="left:241px;top:154px">Children<br>sponsored<br>in India</div>
  <div class="card" style="left:270px;top:151px;width:17px;height:17px;font-size:9px;font-weight:800;text-align:center;line-height:19px">1%</div>
  <div class="a sm" style="left:290px;top:156px">Pledge<br>Partner</div>
</section>

<!-- Customer success -->
<section class="slide c1 r3">
  <div class="hdr" style="width:275px"><h2>CUSTOMER <span>SUCCESS</span></h2></div>
  <div class="dash" style="left:14px;top:36px;width:73px;height:78px"></div>
  <div class="a pinkcap" style="left:36px;top:40px">RESOURCES</div>
  <div class="ico" style="left:20px;top:48px"></div><div class="a lbl" style="left:35px;top:50px">Support Portal</div>
  <div class="ico" style="left:20px;top:64px"></div><div class="a lbl" style="left:35px;top:66px">Product Documentation</div>
  <div class="ico" style="left:20px;top:81px"></div><div class="a lbl" style="left:35px;top:83px">Training Videos</div>
  <div class="ico" style="left:20px;top:97px"></div><div class="a lbl" style="left:35px;top:98px">Community Idea<br>Exchange</div>
  <div class="dash" style="left:14px;top:117px;width:73px;height:56px"></div>
  <div class="a pinkcap" style="left:40px;top:120px">SUPPORT</div>
  <div class="ico" style="left:20px;top:130px"></div><div class="a lbl" style="left:35px;top:132px">Phone</div>
  <div class="ico" style="left:20px;top:146px"></div><div class="a lbl" style="left:35px;top:148px">Email</div>
  <div class="ico" style="left:20px;top:162px"></div><div class="a lbl" style="left:35px;top:164px">Web</div>
  <div class="donut" style="left:58px;top:137px;width:22px;height:22px;background:var(--grey-900)"></div>
  <div class="pill" style="left:94px;top:36px;width:116px;color:var(--ink)">Most customers implement Quorvex in 30 days or less</div>
  <div class="card" style="left:94px;top:45px;width:116px;height:64px">
    <div class="ico" style="left:12px;top:6px;width:13px;height:13px"></div>
    <div class="a pinkcap" style="left:40px;top:8px">PRODUCT INNOVATION</div>
    <div class="a sm" style="left:40px;top:18px">Average 6 releases in an year</div>
    <div class="donut" style="left:26px;top:31px;width:16px;height:16px">45%</div>
    <div class="donut" style="left:72px;top:31px;width:16px;height:16px">55%</div>
    <div class="a sm" style="left:12px;top:50px;width:44px;text-align:center">Enhancements are driven by customers</div>
    <div class="a sm" style="left:60px;top:50px;width:40px;text-align:center">Innovation is driven by Quorvex</div>
  </div>
  <div class="a pinkcap" style="left:100px;top:123px">COMMUNITY</div>
  <div class="ico" style="left:103px;top:136px"></div><div class="a lbl" style="left:121px;top:138px">Community Forum</div>
  <div class="ico" style="left:103px;top:155px"></div><div class="a lbl" style="left:121px;top:158px">Webinar Sessions</div>
  <div class="ico" style="left:166px;top:145px"></div><div class="a lbl" style="left:185px;top:147px">Office Hours</div>
  <div class="a" style="left:217px;top:36px;height:136px;border-left:.6px dashed var(--grey-400)"></div>
  <div class="ico" style="left:229px;top:38px"></div><div class="a lbl" style="left:249px;top:41px">Implementation Partners</div>
  <div class="a sm" style="left:229px;top:57px">Multiple Tier 1 and Tier 2 System Integrators</div>
  <div class="pill" style="left:229px;top:66px;width:26px;height:9px;line-height:8px;color:var(--ink)">TIER 1</div>
  <div class="a" style="left:262px;top:68px;width:12px;height:5px;border:1px solid var(--ink);border-radius:3px"></div>
  <div class="pill" style="left:281px;top:66px;width:26px;height:9px;line-height:8px;color:var(--ink)">TIER 2</div>
  <div class="card" style="left:226px;top:98px;width:82px;height:43px">
    <div class="donut" style="left:32px;top:5px;width:17px;height:17px">98.2%</div>
    <div class="a sm" style="left:14px;top:26px;width:54px;text-align:center">Customers would recommend Quorvex to other</div>
  </div>
  <div class="donut" style="left:232px;top:147px;width:18px;height:18px;background:#fff"></div>
  <div class="a" style="left:259px;top:150px;border-left:.8px solid var(--pink);padding-left:4px"><div style="font-size:6.5px;font-weight:700">103%</div><div class="sm">Revenue retention</div></div>
</section>

<!-- Current customers -->
<section class="slide c2 r3">
  <div class="hdr"><h2>CURRENT <span>CUSTOMERS</span></h2><div class="a" style="left:10px;top:22px;font-size:3.2px;color:#fff">Quorvex is trusted by the largest brands around the world. And the only DevOps solution used by Stratacloud themselves.</div></div>
  <div class="a" style="left:8px;top:52px;width:300px;height:9px;background:var(--grey-900)"></div>
  <div class="cat" style="left:8px">Business<br>Services</div>
  <div class="cat" style="left:41px">Educational &amp;<br>Non-profit</div>
  <div class="cat" style="left:75px">Federal<br>Government</div>
  <div class="cat" style="left:108px">Financial<br>Services</div>
  <div class="cat" style="left:142px">Healthcare &amp;<br>Life Sciences</div>
  <div class="cat" style="left:175px;line-height:7px;padding:0">Industrials</div>
  <div class="cat" style="left:209px">State<br>Government</div>
  <div class="cat" style="left:242px;line-height:7px;padding:0">Technology</div>
  <div class="cat" style="left:276px;line-height:7px;padding:0">Others</div>
  <div class="logo-col" style="left:8px"><i style="width:14px"></i><i style="width:10px"></i><i style="width:16px"></i><i style="width:12px"></i><i style="width:12px"></i><i style="width:18px"></i><i style="width:14px"></i><i style="width:14px"></i><i style="width:16px"></i><i style="width:14px"></i><i style="width:18px"></i></div>
  <div class="logo-col" style="left:41px"><i style="width:7px;height:6px;border-radius:50%"></i><i style="width:14px"></i><i style="width:10px;height:6px"></i><i style="width:14px"></i><i style="width:16px"></i><i style="width:16px"></i><i style="width:16px"></i><i style="width:18px"></i></div>
  <div class="logo-col" style="left:75px"><i style="width:16px"></i><i style="width:10px;height:10px;border-radius:50%"></i><i style="width:12px"></i><i style="width:10px;height:10px;border-radius:50%"></i><i style="width:10px;height:10px;border-radius:50%"></i><i style="width:16px"></i></div>
  <div class="logo-col" style="left:108px"><i style="width:16px"></i><i style="width:10px"></i><i style="width:14px"></i><i style="width:16px"></i><i style="width:16px"></i><i style="width:14px"></i><i style="width:14px"></i><i style="width:16px"></i><i style="width:14px"></i><i style="width:14px"></i><i style="width:16px"></i><i style="width:16px"></i><i style="width:12px"></i></div>
  <div class="logo-col" style="left:142px"><i style="width:18px"></i><i style="width:12px"></i><i style="width:14px"></i><i style="width:12px"></i><i style="width:14px"></i><i style="width:12px"></i><i style="width:16px"></i><i style="width:14px"></i><i style="width:14px"></i><i style="width:12px"></i><i style="width:12px"></i><i style="width:12px"></i></div>
  <div class="logo-col" style="left:175px"><i style="width:18px"></i><i style="width:10px;height:5px"></i><i style="width:12px"></i><i style="width:16px"></i><i style="width:18px"></i><i style="width:8px;height:6px"></i><i style="width:18px"></i><i style="width:16px"></i><i style="width:16px"></i><i style="width:12px;height:5px"></i><i style="width:14px;height:5px"></i></div>
  <div class="logo-col" style="left:209px"><i style="width:12px;height:12px;border-radius:50%"></i><i style="width:12px;height:12px;border-radius:50%"></i><i style="width:16px"></i><i style="width:14px"></i><i style="width:12px"></i></div>
  <div class="logo-col" style="left:242px"><i style="width:12px"></i><i style="width:14px"></i><i style="width:10px;height:5px"></i><i style="width:10px"></i><i style="width:18px"></i><i style="width:14px"></i><i style="width:12px"></i><i style="width:14px"></i><i style="width:10px;height:5px"></i><i style="width:14px"></i><i style="width:14px"></i><i style="width:12px"></i><i style="width:12px"></i><i style="width:16px"></i></div>
  <div class="logo-col" style="left:276px"><i style="width:18px"></i><i style="width:12px"></i><i style="width:10px"></i><i style="width:10px;height:5px"></i><i style="width:12px"></i><i style="width:10px;height:5px"></i><i style="width:8px;height:6px"></i><i style="width:14px"></i><i style="width:12px"></i><i style="width:10px"></i></div>
  <svg class="a" style="left:0;top:62px" width="315" height="115"><g stroke="#999" stroke-width=".5" stroke-dasharray="1 1.2"><line x1="40.5" y1="2" x2="40.5" y2="110"/><line x1="74" y1="2" x2="74" y2="110"/><line x1="107.5" y1="2" x2="107.5" y2="110"/><line x1="141" y1="2" x2="141" y2="110"/><line x1="174.5" y1="2" x2="174.5" y2="110"/><line x1="208" y1="2" x2="208" y2="110"/><line x1="241.5" y1="2" x2="241.5" y2="110"/><line x1="275" y1="2" x2="275" y2="110"/></g></svg>
</section>

<!-- Application development flow -->
<section class="slide c1 r4">
  <div class="dots" role="img" aria-label="Halftone dot wave decoration" style="left:180px;top:-20px;width:160px;height:80px"></div>
  <div class="a" style="left:0;top:9px;width:100%;text-align:center;font-size:10px;font-weight:800">APPLICATION DEVELOPMENT <span class="title-pink">FLOW</span></div>
  <div class="a" style="left:145px;top:24px;width:25px;height:1px;background:var(--pink)"></div>
  <div class="card" style="left:52px;top:41px;width:252px;height:95px;border-radius:9px"></div>
  <div class="a" style="left:284px;top:47px;width:6px;height:6px;border-radius:50%;background:var(--pink)"></div>
  <svg class="a" style="left:0;top:0" width="315" height="177" viewBox="0 0 315 177">
    <g stroke="#999" stroke-width=".5" stroke-dasharray="1 1" fill="none">
      <path d="M24 57H50M24 85H50M24 114H50"/>
      <path d="M158 56H198V78M158 89H186M158 119H198V97"/>
      <path d="M210 88H222M262 88H272"/>
      <path d="M230 98V120H208V144M242 98V144M254 98V120H281V144"/>
      <path d="M82 56H92M82 89H92M82 119H92"/>
    </g>
    <g fill="#fff" stroke="#444" stroke-width=".5"><circle cx="74" cy="57" r="7"/><circle cx="74" cy="89" r="7"/><circle cx="74" cy="119" r="7"/></g>
    <g font-family="Montserrat,sans-serif" font-size="8" fill="#bbb" text-anchor="middle"><text x="69" y="61">1</text><text x="69" y="93">2</text><text x="69" y="123">3</text></g>
  </svg>
  <div class="ico" style="left:12px;top:52px"></div><div class="a lbl" style="left:11px;top:63px;font-size:3.6px">TEAM 1</div>
  <div class="ico" style="left:12px;top:80px"></div><div class="a lbl" style="left:11px;top:91px;font-size:3.6px">TEAM 2</div>
  <div class="ico" style="left:12px;top:109px"></div><div class="a lbl" style="left:11px;top:120px;font-size:3.6px">TEAM 3</div>
  <div class="a lbl" style="left:64px;top:45px;font-size:3.6px">Snapshot</div>
  <div class="a lbl" style="left:64px;top:77px;font-size:3.6px">Snapshot</div>
  <div class="a lbl" style="left:64px;top:107px;font-size:3.6px">Snapshot</div>
  <div class="dash" style="left:92px;top:48px;width:66px;height:23px"></div>
  <div class="pill" style="left:96px;top:51px;width:58px;color:var(--ink)">Feature Branch 1</div>
  <div class="a" style="left:96px;top:59px;width:58px;height:3.5px;background:var(--pink);border-radius:2px;color:#fff;font-size:2.8px;text-align:center;line-height:3.5px">Tag components to User Story</div>
  <div class="a" style="left:96px;top:64px;width:28px;height:3.5px;background:var(--pink);border-radius:2px;color:#fff;font-size:2.8px;text-align:center;line-height:3.5px">Static Analysis</div>
  <div class="a" style="left:126px;top:64px;width:28px;height:3.5px;background:var(--pink);border-radius:2px;color:#fff;font-size:2.8px;text-align:center;line-height:3.5px">Peer Code Review</div>
  <div class="dash" style="left:92px;top:81px;width:66px;height:16px"></div>
  <div class="pill" style="left:96px;top:85px;width:58px;color:var(--ink)">Feature Branch 2</div>
  <div class="dash" style="left:92px;top:111px;width:66px;height:16px"></div>
  <div class="pill" style="left:96px;top:115px;width:58px;color:var(--ink)">Feature Branch 3</div>
  <div class="a" style="left:186px;top:78px;width:24px;height:20px;background:var(--grey-900);border-radius:2px;color:#fff;font-size:3.6px;font-weight:700;text-align:center;padding-top:5px;line-height:1.2">Release<br>Branch</div>
  <div class="a" style="left:222px;top:78px;width:40px;height:20px;background:var(--grey-900);border-radius:2px;color:#fff;font-size:3.6px;font-weight:700;text-align:center;padding-top:5px;line-height:1.2">DEPLOYMENT<br><span style="font-weight:500">Manual/Automatic</span></div>
  <div class="a" style="left:272px;top:78px;width:25px;height:20px;background:var(--grey-900);border-radius:2px;color:#fff;font-size:3.4px;font-weight:700;text-align:center;padding-top:11px">Repository</div>
  <div class="card" style="left:196px;top:144px;width:24px;height:12px;border-radius:6px;font-size:3.6px;font-weight:600;text-align:center;line-height:12px">QA</div>
  <div class="card" style="left:230px;top:144px;width:24px;height:12px;border-radius:6px;font-size:3.6px;font-weight:600;text-align:center;line-height:12px">UAT</div>
  <div class="card" style="left:266px;top:144px;width:30px;height:12px;border-radius:6px;font-size:3.6px;font-weight:600;text-align:center;line-height:12px">PRODUCTION</div>
</section>

<!-- Side-by-side -->
<section class="slide c2 r4">
  <div class="hdr"><h2>SIDE-BY-SIDE <span>DIFFERENCES</span></h2></div>
  <div class="card" style="left:13px;top:39px;width:90px;height:130px;border-radius:8px">
    <div class="a" style="left:12px;top:6px;font-size:7px;font-weight:500;color:var(--grey-600);line-height:1.25">Custom-Built<br>Solutions</div>
    <div class="ico" style="left:70px;top:8px;width:11px;height:11px"></div>
    <div class="a" style="left:6px;top:10px;height:116px;border-left:.6px dashed var(--grey-400)"></div>
    <div class="pill" style="left:11px;top:42px;width:73px;height:8px;line-height:7px">Regression Testing</div>
    <div class="pill" style="left:11px;top:58px;width:73px;height:8px;line-height:7px">Scripts</div>
    <div class="pill" style="left:11px;top:72px;width:73px;height:11px;line-height:3.8px;padding-top:1px">Deployment Using Open Source Pipelines</div>
    <div class="pill" style="left:11px;top:87px;width:73px;height:26px;line-height:25px;box-shadow:0 1px 3px rgba(0,0,0,.2)">Git Repository</div>
  </div>
  <div class="dash" style="left:112px;top:39px;width:88px;height:130px;border-radius:8px"></div>
  <div class="a" style="left:124px;top:45px;font-size:7px;font-weight:500;line-height:1.25">Other<br>AppMarket<br>Solutions</div>
  <div class="ico" style="left:178px;top:47px;width:11px;height:11px"></div>
  <div class="a" style="left:118px;top:49px;height:116px;border-left:.6px dashed var(--grey-600)"></div>
  <div class="pill" style="left:122px;top:97px;width:73px;height:8px;line-height:7px;color:var(--ink);box-shadow:0 1px 2px rgba(0,0,0,.2)">Regression Testing</div>
  <div class="pill" style="left:122px;top:114px;width:73px;height:8px;line-height:7px;color:var(--ink);box-shadow:0 1px 2px rgba(0,0,0,.2)">Deployment Using Git Branches</div>
  <div class="pill" style="left:122px;top:127px;width:73px;height:32px;line-height:31px;color:var(--ink);background:var(--grey-100);box-shadow:0 1px 3px rgba(0,0,0,.25)">Git Repository</div>
  <div class="card" style="left:211px;top:36px;width:90px;height:136px;border-radius:8px">
    <div class="a" style="left:11px;top:7px;font-size:7px;font-weight:500;color:var(--pink)">Quorvex</div>
    <div class="a" style="left:70px;top:7px;width:10px;height:10px;border-radius:50%;border:1px solid var(--pink)"></div>
    <div class="a" style="left:7px;top:14px;height:118px;border-left:.6px dashed var(--pink)"></div>
    <div class="pill pk" style="left:11px;top:23px;width:73px">Insight Analytics/Prediction</div>
    <div class="pill pk" style="left:11px;top:33px;width:73px">Regression Testing</div>
    <div class="pill pk" style="left:11px;top:43px;width:73px">Admin Tools</div>
    <div class="pill pk" style="left:11px;top:54px;width:73px">Regression Testing</div>
    <div class="pill pk" style="left:11px;top:64px;width:73px">Stratacloud-Specific Native Pipelines</div>
    <div class="pill pk" style="left:11px;top:74px;width:73px">Code Reviews</div>
    <div class="pill pk" style="left:11px;top:84px;width:73px">Impact Analysis</div>
    <div class="pill pk" style="left:11px;top:94px;width:73px">Org Synchronization</div>
    <div class="pill pk" style="left:11px;top:104px;width:73px">Dependencies</div>
    <div class="pill pk" style="left:11px;top:115px;width:73px">Git Repository</div>
  </div>
</section>

<!-- Maturity model -->
<section class="slide c1 r5">
  <div class="a" style="left:17px;top:17px;font-size:10px;font-weight:800">MATURITY <span class="title-pink">MODEL</span></div>
  <div class="a" style="left:17px;top:32px;width:25px;height:1px;background:var(--pink)"></div>
  <svg class="a" style="left:0;top:0" width="315" height="177" viewBox="0 0 315 177">
    <g fill="#1c1c1c">
      <path d="M39 95h5v62h-5zM36.5 95l5-7 5 7z"/>
      <path d="M90 82h5v75h-5zM87.5 82l5-7 5 7z"/>
      <path d="M139 62h5v95h-5zM136.5 62l5-7 5 7z"/>
      <path d="M193 43h5v114h-5zM190.5 43l5-7 5 7z"/>
      <path d="M246 29h5v128h-5zM243.5 29l5-7 5 7z"/>
    </g>
    <g fill="#fff" stroke="#333" stroke-width=".5">
      <circle cx="41.5" cy="111" r="5"/><circle cx="41.5" cy="140" r="5"/>
      <circle cx="92.5" cy="98" r="5"/><circle cx="92.5" cy="130" r="5"/>
      <circle cx="141.5" cy="77" r="5"/><circle cx="141.5" cy="97" r="5"/><circle cx="141.5" cy="125" r="5"/>
      <circle cx="195.5" cy="59" r="5"/><circle cx="195.5" cy="89" r="5"/><circle cx="195.5" cy="120" r="5"/>
      <circle cx="248.5" cy="46" r="5"/><circle cx="248.5" cy="107" r="5"/>
    </g>
    <g stroke="#999" stroke-width=".5" stroke-dasharray="1 1"><path d="M47 111h18M47 140h18M98 98h17M98 130h17M147 77h18M147 97h18M147 125h18M201 59h17M201 89h17M201 120h17M254 46h17M254 107h17"/></g>
  </svg>
  <div class="a lbl" style="left:32px;top:79px;font-size:3.8px;color:var(--grey-600)">LEVEL 1</div>
  <div class="a lbl" style="left:83px;top:66px;font-size:3.8px;color:var(--grey-600)">LEVEL 2</div>
  <div class="a lbl" style="left:132px;top:47px;font-size:3.8px;color:var(--grey-600)">LEVEL 3</div>
  <div class="a lbl" style="left:186px;top:28px;font-size:3.8px;color:var(--grey-600)">LEVEL 4</div>
  <div class="a lbl" style="left:240px;top:14px;font-size:3.8px;color:var(--grey-600)">LEVEL 5</div>
  <div class="a lbl" style="left:50px;top:111px;font-weight:500">No manual<br>deployments</div>
  <div class="a lbl" style="left:50px;top:140px;font-weight:500">Adhoc<br>component<br>Releases</div>
  <div class="a lbl" style="left:101px;top:100px;font-weight:500">Documented<br>processes</div>
  <div class="a lbl" style="left:101px;top:132px;font-weight:500">Version<br>control as<br>the source<br>of truth</div>
  <div class="a lbl" style="left:152px;top:79px;font-weight:500">Merging<br>multiple user<br>stories</div>
  <div class="a lbl" style="left:152px;top:103px;font-weight:500">Collaboration<br>between the<br>team</div>
  <div class="a lbl" style="left:152px;top:128px;font-weight:500">Proactive<br>monitoring<br>of code<br>coverage,<br>testing and<br>code reviews</div>
  <div class="a lbl" style="left:206px;top:62px;font-weight:500">Minimal steps</div>
  <div class="a lbl" style="left:206px;top:91px;font-weight:500">Full end-to-end<br>compliance</div>
  <div class="a lbl" style="left:206px;top:122px;font-weight:500">Regression<br>testing 04</div>
  <div class="a lbl" style="left:260px;top:48px;font-weight:500">Continuous<br>Delivery via<br>Pipelines</div>
  <div class="a lbl" style="left:261px;top:110px;font-weight:500">Complete end-<br>to-end DevOps<br>metrics on<br>developer<br>productivity,<br>lead time,<br>deployment fail<br>rate, etc</div>
  <div class="a pinkcap" style="left:32px;top:163px">ADHOC</div>
  <div class="a pinkcap" style="left:83px;top:163px">DEFINED</div>
  <div class="a pinkcap" style="left:130px;top:163px">MANAGED</div>
  <div class="a pinkcap" style="left:182px;top:163px">OPTIMIZED</div>
  <div class="a pinkcap" style="left:228px;top:163px">MEASURED &amp; PREDICTABLE</div>
</section>

<!-- Current state -->
<section class="slide c2 r5">
  <div class="hdr"><h2>CURRENT <span>STATE</span></h2></div>
  <svg class="a" style="left:0;top:0" width="315" height="177" viewBox="0 0 315 177">
    <circle cx="154" cy="98" r="52" fill="#fff" stroke="#ddd" stroke-width="1.5"/>
    <g fill="none" stroke="#333" stroke-width=".4"><circle cx="154" cy="98" r="40"/><circle cx="154" cy="98" r="31"/><circle cx="154" cy="98" r="22"/><circle cx="154" cy="98" r="13"/></g>
    <line x1="112" y1="73" x2="134" y2="97" stroke="#ea0a8e" stroke-width=".6" stroke-dasharray="1 1"/>
    <circle cx="134" cy="97" r="2" fill="#ea0a8e"/>
  </svg>
  <div class="ico" style="left:150px;top:47px"></div><div class="a lbl" style="left:122px;top:38px">Automated deployments (3)</div>
  <div class="ico" style="left:107px;top:69px"></div><div class="a lbl" style="left:57px;top:71px">User Story Tracking</div>
  <div class="ico" style="left:193px;top:70px"></div><div class="a lbl" style="left:205px;top:70px">Defined Application<br>Development Process (4)</div>
  <div class="ico" style="left:98px;top:114px"></div><div class="a lbl" style="left:56px;top:116px">Compliance (4)</div>
  <div class="ico" style="left:203px;top:114px"></div><div class="a lbl" style="left:216px;top:116px">Continuous Delivery (3)</div>
  <div class="ico" style="left:122px;top:146px"></div><div class="a lbl" style="left:92px;top:159px">Testing (2)</div>
  <div class="ico" style="left:185px;top:146px"></div><div class="a lbl" style="left:196px;top:157px">Code Quality (4)</div>
</section>

<!-- Q and A -->
<section class="slide c1 r6">
  <div class="hdr" style="width:275px"><h2>Q AND <span>A SLIDE</span></h2></div>
  <div class="card" style="left:18px;top:40px;width:132px;height:129px;border-radius:8px">
    <div class="pill" style="left:15px;top:6px;width:55px;color:var(--ink)">QUESTIONS</div>
    <div class="a" style="left:6px;top:10px;height:113px;border-left:.6px dashed var(--grey-400)"></div>
    <div class="a qa" style="left:14px;top:24px"><b>1.</b> Lorem ipsum dolor sit amet, consectetuer<br>&nbsp;&nbsp;&nbsp;&nbsp;adipiscing elit, ?</div>
    <div class="a qa" style="left:14px;top:40px"><b>2.</b> Lorem ipsum dolor sit amet, consectetuer<br>&nbsp;&nbsp;&nbsp;&nbsp;adipiscing elit, ?</div>
    <div class="a qa" style="left:14px;top:56px"><b>3.</b> Lorem ipsum dolor sit amet, consectetuer<br>&nbsp;&nbsp;&nbsp;&nbsp;adipiscing elit, ?</div>
    <div class="a qa" style="left:14px;top:73px"><b>4.</b> Lorem ipsum dolor sit amet, consectetuer<br>&nbsp;&nbsp;&nbsp;&nbsp;adipiscing elit, ?</div>
    <div class="a qa" style="left:14px;top:89px"><b>5.</b> Lorem ipsum dolor sit amet, consectetuer<br>&nbsp;&nbsp;&nbsp;&nbsp;adipiscing elit, ?</div>
  </div>
  <div class="card" style="left:165px;top:40px;width:132px;height:129px;border-radius:8px">
    <div class="pill pk" style="left:65px;top:6px;width:55px">ANSWERS</div>
    <div class="a" style="left:126px;top:10px;height:113px;border-left:.6px dashed var(--grey-400)"></div>
    <div class="a qa" style="right:12px;top:25px;text-align:right">Lorem ipsum dolor sit amet, consectetuer <b>1.</b><br>adipiscing elit&nbsp;&nbsp;&nbsp;&nbsp;&nbsp;</div>
    <div class="a qa" style="right:12px;top:41px;text-align:right">Lorem ipsum dolor sit amet, consectetuer <b>2.</b><br>adipiscing elit,&nbsp;&nbsp;&nbsp;&nbsp;&nbsp;</div>
    <div class="a qa" style="right:12px;top:57px;text-align:right">Lorem ipsum dolor sit amet, consectetuer <b>3.</b><br>adipiscing elit,&nbsp;&nbsp;&nbsp;&nbsp;&nbsp;</div>
    <div class="a qa" style="right:12px;top:74px;text-align:right">Lorem ipsum dolor sit amet, consectetuer <b>4.</b><br>adipiscing elit,&nbsp;&nbsp;&nbsp;&nbsp;&nbsp;</div>
    <div class="a qa" style="right:12px;top:90px;text-align:right">Lorem ipsum dolor sit amet, consectetuer <b>5.</b><br>adipiscing elit,&nbsp;&nbsp;&nbsp;&nbsp;&nbsp;</div>
  </div>
  <div class="a" style="left:133px;top:86px;width:24px;height:24px;border-radius:50%;background:var(--grey-900);color:#fff;font-size:10px;font-weight:700;text-align:center;line-height:24px">Q</div>
  <div class="a" style="left:158px;top:86px;width:24px;height:24px;border-radius:50%;background:var(--grey-900);color:#fff;font-size:10px;font-weight:700;text-align:center;line-height:24px">A</div>
</section>

<!-- Thank you -->
<section class="slide c2 r6 grad-bg">
  <div class="dots" role="img" aria-label="Halftone dot wave decoration" style="left:-10px;top:70px;width:330px;height:90px"></div>
  <div class="a" style="left:15px;top:40px;font-size:14px;font-weight:800">THANK <span class="title-pink">YOU</span></div>
  <div class="a" style="left:15px;top:60px;width:25px;height:1px;background:var(--pink)"></div>
  <div class="foot" style="background:transparent;height:18px;font-size:4px"><span>www.quorvex.example</span><span>(555) 014 2280</span><span>hello [@] quorvex.example</span></div>
  <div class="brand" style="right:10px;top:161px;font-size:12px"><span class="mark" style="width:7px;height:7px"></span>Quorvex</div>
</section>

</body>
</html>
```